BRIGHTWAVE DENTAL *

please see attached.

Target Market(s)

Adults 18-60

Contact Information for Business Card

Website: brightwavedentalqz.com
Phone number 555 304 7726 email: brightwavedentalqz@mailvex.com
Address:417 S. Kellim rd
Suite#24, TX70000
Dr. Elias Varno, DDS

Font styles to use
Sans Serif

Requirements
Must have
• Logo, phone number website, doctor,
• 's name

```html
<!DOCTYPE html>
<html lang="en">
<head>
<meta charset="utf-8">
<title>Brightwave Dental – Business Card</title>
<link rel="stylesheet" href="https://fonts.googleapis.com/css2?family=Montserrat:wght@400;600;700&family=Quicksand:wght@500&display=swap">
<style>
  :root {
    --stage: #2b2b2d;
    --navy: #0f2540;
    --navy-deep: #0a1a2e;
    --teal: #1b8a9a;
    --ink: #1b1f27;
    --paper: #f4f5f7;
    --logo-light: #d9dde3;
  }
  * { margin: 0; padding: 0; box-sizing: border-box; }
  html, body { width: 1200px; height: 997px; overflow: hidden; }
  body { background: var(--stage); font-family: "Montserrat", sans-serif; position: relative; }

  .card {
    position: absolute;
    top: 343px;
    width: 540px;
    height: 310px;
    border-radius: 16px;
    overflow: hidden;
  }
  .card--front { left: 40px; background: linear-gradient(160deg, #13304f, var(--navy-deep)); }
  .card--back { left: 620px; background: var(--paper); }

  .card__shapes { position: absolute; inset: 0; }

  .brand {
    position: absolute;
    left: 0; right: 0;
    display: flex;
    flex-direction: column;
    align-items: center;
  }
  .brand__mark {
    width: 62px; height: 62px;
    border-radius: 50%;
    border: 1.5px solid currentColor;
  }
  .brand__name {
    margin-top: 14px;
    font-family: "Quicksand", sans-serif;
    font-weight: 500;
    font-size: 27px;
    letter-spacing: 2px;
    white-space: nowrap;
  }
  .card--front .brand { top: 98px; color: var(--logo-light); }
  .card--back .brand { top: 24px; color: var(--ink); }
  .card--back .brand__name { margin-top: 12px; font-size: 25px; }

  .holder { position: absolute; left: 28px; top: 160px; }
  .holder__name { font-weight: 700; font-size: 15px; color: var(--teal); letter-spacing: 0.5px; white-space: nowrap; }
  .holder__role { font-size: 11.5px; color: var(--ink); margin-top: 1px; }

  .contacts { position: absolute; left: 28px; top: 208px; list-style: none; }
  .contacts li {
    display: flex; align-items: center; gap: 12px;
    font-size: 12px; color: var(--ink); height: 23px; white-space: nowrap;
  }
  .contacts svg { width: 14px; height: 14px; flex: none; }

  .address {
    position: absolute; right: 30px; top: 170px;
    text-align: right; font-size: 11px; line-height: 1.35; color: var(--teal);
  }
  .website {
    position: absolute; right: 26px; top: 273px;
    font-size: 12px; font-weight: 600; letter-spacing: 0.6px; color: #ffffff;
  }
</style>
</head>
<body>

<section class="card card--front" aria-label="Business card front">
  <div class="brand">
    <span class="brand__mark"></span>
    <span class="brand__name">BRIGHTWAVE DENTAL</span>
  </div>
</section>

<section class="card card--back" aria-label="Business card back">
  <svg class="card__shapes" viewBox="0 0 540 310" aria-hidden="true">
    <line x1="196" y1="172" x2="512" y2="150" stroke="#1b1f27" stroke-width="1"/>
    <path d="M300,310 C322,310 318,258 352,258 L540,258 L540,310 Z" fill="var(--navy)"/>
    <path d="M0,292 L292,285 Q312,284 322,266 L334,266 Q322,294 296,296 L0,302 Z" fill="var(--teal)"/>
    <path d="M0,302 L296,296 Q322,294 334,266 L340,266 Q328,300 298,302 L0,310 Z" fill="var(--navy)"/>
  </svg>

  <div class="brand">
    <span class="brand__mark"></span>
    <span class="brand__name">BRIGHTWAVE DENTAL</span>
  </div>

  <div class="holder">
    <p class="holder__name">DR. ELIAS VARNO</p>
    <p class="holder__role">DDS</p>
  </div>

  <ul class="contacts">
    <li>
      <svg viewBox="0 0 14 14"><circle cx="7" cy="7" r="7" fill="var(--teal)"/><path d="M4.4,3.6 l1.3,0 0.6,1.7 -0.8,0.7 q0.7,1.5 2.4,2.4 l0.7,-0.8 1.7,0.6 0,1.3 q-3.9,0.5 -5.9,-5.9z" fill="#fff"/></svg>
      555 304 7726
    </li>
    <li>
      <svg viewBox="0 0 14 14"><circle cx="7" cy="7" r="7" fill="var(--teal)"/><rect x="3.5" y="4.5" width="7" height="5" fill="none" stroke="#fff" stroke-width="0.9"/><path d="M3.5,4.5 L7,7.3 L10.5,4.5" fill="none" stroke="#fff" stroke-width="0.9"/></svg>
      brightwavedentalqz@mailvex.com
    </li>
    <li>
      <svg viewBox="0 0 14 14"><circle cx="7" cy="7" r="7" fill="var(--teal)"/><circle cx="7" cy="7" r="3" fill="#fff"/></svg>
      eliasvarno
    </li>
  </ul>

  <p class="address">417 S. Kellim rd<br>Suite#24, TX70000</p>
  <p class="website">www.brightwavedentalqz.com</p>
</section>

</body>
</html>
```